Stationary and biz card for events management company
Plume Events
Stationary and biz card for events management  company - Events
Creative Brief
Professional
Owen Harte
42 Delwyn Street, Southport, Merseyside. PR9 7QT
info@plume-events.co.uk
www.plume-events.co.uk
Please don't include my address on the business card, all contact info to be included on letterhead. I am considering having my business cards printed on the plastic credit card type material. Due to the many finishes available with the plastic cards a unique design may work very well. Please have a look at one of the many plastic card websites, you will see that they do finishes such as matt black or transparent. I am open to ideas as to the finish, the ones I mentioned are just examples.
I'm open to ideas, just the logo or maybe a brief outline of what we do; Event Management, Equipment Hire, Event Packages

```html
<!DOCTYPE html>
<html lang="en">
<head>
<meta charset="utf-8">
<title>Plume Events – Stationery</title>
<link rel="stylesheet" href="https://fonts.googleapis.com/css2?family=Montserrat:wght@400;700&family=Open+Sans:wght@400;600&display=swap">
<style>
:root{
  --red:#c8161d;
  --red-dark:#8e0c12;
  --grey:#9a9a9a;
  --grey-light:#e3e3e3;
  --ink:#333;
  --paper:#fff;
  --black:#141414;
  --stage:#ece7df;
}
*{box-sizing:border-box;margin:0;padding:0}
html,body{width:1200px;height:319px;overflow:hidden;background:var(--stage);font-family:"Open Sans",Arial,sans-serif;color:var(--ink)}
.canvas{position:relative;width:1200px;height:319px}
.piece{position:absolute;box-shadow:0 2px 6px rgba(0,0,0,.25);overflow:hidden}
.label{position:absolute;font-size:7px;color:#6c645a;text-align:center;font-family:"Open Sans",Arial,sans-serif}
.brand{font-family:"Montserrat",Arial,sans-serif;font-weight:700;color:var(--red);letter-spacing:.5px;display:flex;align-items:center;gap:4px;white-space:nowrap}
.brand .mark{display:inline-block;background:var(--red);flex:none}
.brand.light{color:#fff}
.brand.light .mark{background:#fff}
.tiny{font-size:5px;line-height:1.5}

/* business cards */
.card-front{left:8px;top:132px;width:140px;height:62px;background:var(--paper);border-left:8px solid var(--red);padding:8px 10px}
.card-front .brand{font-size:10px}
.card-front .brand .mark{width:9px;height:9px}
.card-front .contact{margin-top:7px}
.card-front .name{font-size:7px;font-weight:600;color:var(--red)}
.card-back{left:8px;top:202px;width:140px;height:62px;background:var(--black);display:flex;align-items:center;justify-content:center;border-right:8px solid var(--red)}
.card-back .brand{font-size:10px}
.card-back .brand .mark{width:9px;height:9px}

/* letterhead */
.letterhead{left:162px;top:28px;width:196px;height:262px;background:var(--paper);padding:16px 14px 14px 22px}
.letterhead::before{content:"";position:absolute;left:0;top:0;bottom:0;width:8px;background:var(--red)}
.letterhead .brand{font-size:12px}
.letterhead .brand .mark{width:10px;height:10px}
.letterhead .recipient{margin-top:16px}
.letterhead .body{margin-top:10px;font-size:5px;line-height:1.7}
.letterhead .body p{margin-bottom:6px}
.letterhead .sign{margin-top:12px;font-size:8px;font-weight:600;color:var(--red)}
.letterhead .foot{position:absolute;left:22px;right:14px;bottom:12px;border-top:1px solid var(--grey-light);padding-top:4px;color:var(--grey)}

/* compliment slip */
.slip{left:368px;top:34px;width:114px;height:52px;background:var(--paper);border-top:5px solid var(--red);padding:7px 8px}
.slip .brand{font-size:8px}
.slip .brand .mark{width:7px;height:7px}
.slip .title{margin-top:6px;font-size:6px;font-weight:600;color:var(--red)}
.slip-back{left:368px;top:96px;width:114px;height:52px;background:var(--paper);border-bottom:5px solid var(--red);padding:8px}

/* envelope */
.envelope{left:368px;top:190px;width:212px;height:100px;background:var(--paper);padding:10px 12px}
.envelope .brand{font-size:9px}
.envelope .brand .mark{width:8px;height:8px}
.envelope .band{position:absolute;left:0;right:0;bottom:0;height:6px;background:var(--red)}

/* dark envelopes */
.env-dark{left:612px;width:200px;height:58px;background:var(--black)}
.env-dark svg{position:absolute;inset:0}
.env-dark .brand{position:absolute;left:78px;top:34px;font-size:8px}
.env-dark .brand .mark{width:7px;height:7px}
.env-dark.one{top:100px}
.env-dark.two{top:166px;background:#fff}
.env-dark.three{top:230px}

/* folder */
.folder{left:830px;top:24px;width:358px;height:268px;display:flex}
.folder .inside{position:relative;width:50%;background:var(--paper);border-right:1px solid #ccc}
.folder .pocket{position:absolute;left:0;right:0;bottom:0;height:92px;background:var(--red);clip-path:polygon(0 22%,100% 0,100% 100%,0 100%)}
.folder .cover{position:relative;width:50%;background:radial-gradient(circle at 40% 45%,#e0282f 0%,var(--red) 45%,var(--red-dark) 100%)}
.folder .cover-band{position:absolute;left:0;right:0;top:40px;height:44px;background:var(--paper);display:flex;align-items:center;padding-left:14px;border-right:18px solid var(--grey)}
.folder .cover-band .brand{font-size:14px}
.folder .cover-band .brand .mark{width:12px;height:12px}
.folder .cover-foot{position:absolute;left:14px;bottom:14px;color:#fff}
</style>
</head>
<body>
<main class="canvas">

  <section class="piece card-front">
    <div class="brand"><span class="mark"></span>PLUME EVENTS</div>
    <div class="contact tiny">
      <div class="name">Owen Harte</div>
      <div>Director</div>
      <div>info@plume-events.co.uk</div>
      <div>www.plume-events.co.uk</div>
    </div>
  </section>
  <section class="piece card-back">
    <div class="brand light"><span class="mark"></span>PLUME EVENTS</div>
  </section>
  <div class="label" style="left:8px;top:270px;width:140px">Business Card</div>

  <section class="piece letterhead">
    <div class="brand"><span class="mark"></span>PLUME EVENTS</div>
    <div class="recipient tiny"><div>Dear Client,</div></div>
    <div class="body">
      <p>Thank you for choosing us to plan your next event. We handle event management, equipment hire and complete event packages across the North West.</p>
      <p>Yours sincerely,</p>
    </div>
    <div class="sign">Owen Harte</div>
    <div class="foot tiny">42 Delwyn Street, Southport, Merseyside. PR9 7QT · info@plume-events.co.uk · www.plume-events.co.uk</div>
  </section>
  <div class="label" style="left:162px;top:294px;width:196px">Letterhead</div>

  <section class="piece slip">
    <div class="brand"><span class="mark"></span>PLUME EVENTS</div>
    <div class="title">With Compliments</div>
  </section>
  <section class="piece slip-back">
    <div class="tiny">www.plume-events.co.uk</div>
  </section>
  <div class="label" style="left:368px;top:152px;width:114px">Compliment Slip</div>

  <section class="piece envelope">
    <div class="brand"><span class="mark"></span>PLUME EVENTS</div>
    <div class="tiny" style="margin-top:4px">42 Delwyn Street, Southport, Merseyside. PR9 7QT</div>
    <div class="band"></div>
  </section>
  <div class="label" style="left:368px;top:294px;width:212px">Envelope</div>

  <section class="piece env-dark one">
    <svg viewBox="0 0 200 58" preserveAspectRatio="none"><polygon points="0,0 200,0 100,30" fill="var(--red)"/></svg>
    <div class="brand light"><span class="mark"></span>PLUME EVENTS</div>
  </section>
  <section class="piece env-dark two">
    <svg viewBox="0 0 200 58" preserveAspectRatio="none"><polygon points="0,0 200,0 100,30" fill="var(--red)"/></svg>
    <div class="brand"><span class="mark"></span>PLUME EVENTS</div>
  </section>
  <section class="piece env-dark three">
    <svg viewBox="0 0 200 58" preserveAspectRatio="none"><polygon points="0,0 200,0 100,30" fill="#2a2a2a"/></svg>
    <div class="brand light"><span class="mark"></span>PLUME EVENTS</div>
  </section>

  <section class="piece folder">
    <div class="inside"><div class="pocket"></div></div>
    <div class="cover">
      <div class="cover-band">
        <div class="brand"><span class="mark"></span>PLUME EVENTS</div>
      </div>
      <div class="cover-foot tiny">www.plume-events.co.uk</div>
    </div>
  </section>
  <div class="label" style="left:830px;top:296px;width:358px">Folder</div>

</main>
</body>
</html>
```